Comprehensive Branding Development for Brightvale Holdings Limited

We have our logo and are seeking a talented graphic designer to help us develop a cohesive branding guideline based on this logo provided by our client.
The goal is to create a comprehensive branding package for various office stationery items and promotional materials.

Deliverables:

The designer will be responsible for creating branding guidelines for the following items:

Letterhead
Envelope
Business card
Key holders
T-shirts
Face cap
Car branding
Pen
Dangler (Air Fresheners)
Lapel pin
PowerPoint template
ID card
Carrier bag
Notebook
Mug cup
Umbrella

Logo Text

Logo Provided by client and no needs for designing a new logo

```html
<!DOCTYPE html>
<html lang="en">
<head>
<meta charset="utf-8">
<title>Brightvale Holdings Limited – Business Card</title>
<link rel="stylesheet" href="https://fonts.googleapis.com/css2?family=Open+Sans:wght@400;600;700&display=swap">
<style>
  :root {
    --backdrop: #575757;
    --brand-red: #ee3639;
    --paper: #fefefe;
    --ink-grey: #8a8a8a;
    --white: #ffffff;
  }
  * { margin: 0; padding: 0; box-sizing: border-box; }
  html, body {
    width: 1199px; height: 1200px; overflow: hidden;
    background: var(--backdrop);
    font-family: "Open Sans", Arial, sans-serif;
  }
  .stage { position: relative; width: 1199px; height: 1200px; }
  .card {
    position: absolute; left: 343px; width: 513px; height: 297px; overflow: hidden;
  }
  .card--front { top: 283px; background: var(--brand-red); }
  .card--back { top: 621px; background: var(--paper); }
  .card__shapes { position: absolute; inset: 0; width: 100%; height: 100%; }

  .brand-name {
    position: absolute; display: flex; align-items: center; gap: 10px;
    font-weight: 400; line-height: 1; text-transform: uppercase;
  }
  .brand-name__mark { flex: none; }
  .brand-name__text span { display: block; }

  .card--front .brand-name { left: 186px; top: 116px; color: var(--white); }
  .card--front .brand-name__mark { width: 44px; height: 44px; background: var(--white); }
  .card--front .brand-name__line1 { font-size: 36px; letter-spacing: 0.5px; }
  .card--front .brand-name__line2 { font-size: 21.5px; margin-top: 6px; }

  .card--back .brand-name { left: 285px; top: 113px; color: var(--brand-red); }
  .card--back .brand-name__mark { width: 32px; height: 32px; background: var(--brand-red); }
  .card--back .brand-name__line1 { font-size: 25px; letter-spacing: 0.3px; }
  .card--back .brand-name__line2 { font-size: 15px; margin-top: 4px; }

  .contact { position: absolute; left: 26px; top: 80px; }
  .contact__name { font-size: 19px; font-weight: 700; color: var(--ink-grey); line-height: 1.1; }
  .contact__role { font-size: 15px; color: var(--brand-red); margin-top: 3px; }
  .contact__list { list-style: none; margin-top: 12px; }
  .contact__item {
    display: flex; align-items: center; gap: 12px;
    font-size: 15.5px; color: var(--ink-grey); height: 27px;
  }
  .contact__item--email { color: var(--brand-red); }
  .contact__icon { width: 11px; height: 11px; flex: none; }
</style>
</head>
<body>
<main class="stage">
  <section class="card card--front" aria-label="Business card front">
    <svg class="card__shapes" viewBox="0 0 513 297" aria-hidden="true">
      <polygon points="0,0 128,148 0,297" fill="var(--white)"/>
    </svg>
    <div class="brand-name">
      <span class="brand-name__mark"></span>
      <div class="brand-name__text">
        <span class="brand-name__line1">Brightvale</span>
        <span class="brand-name__line2">Holdings Limited</span>
      </div>
    </div>
  </section>

  <section class="card card--back" aria-label="Business card back">
    <svg class="card__shapes" viewBox="0 0 513 297" aria-hidden="true">
      <polygon points="102,0 411,0 256,45" fill="var(--brand-red)"/>
      <polygon points="102,297 256,252 411,297" fill="var(--brand-red)"/>
    </svg>
    <div class="contact">
      <p class="contact__name">NAME</p>
      <p class="contact__role">Sales Manager</p>
      <ul class="contact__list">
        <li class="contact__item">
          <svg class="contact__icon" viewBox="0 0 12 12"><path d="M2.5 0.5 L4.5 0.5 L5 3.5 L3.8 4.5 Q5 7.2 7.5 8.2 L8.5 7 L11.5 7.5 L11.5 9.5 Q11 11.5 9 11.5 Q1 10 0.5 2.5 Q0.5 0.8 2.5 0.5Z" fill="var(--ink-grey)"/></svg>
          222 333 444 555
        </li>
        <li class="contact__item contact__item--email">
          <svg class="contact__icon" viewBox="0 0 12 12"><rect x="0" y="2" width="12" height="8" fill="var(--brand-red)"/><path d="M0.5 2.5 L6 6.5 L11.5 2.5" stroke="var(--white)" fill="none" stroke-width="1"/></svg>
          hello@brightvaleholdings.com
        </li>
        <li class="contact__item">
          <svg class="contact__icon" viewBox="0 0 12 12"><circle cx="6" cy="6" r="5.5" fill="var(--ink-grey)"/><path d="M0.5 6 H11.5 M6 0.5 V11.5 M1.5 3.5 H10.5 M1.5 8.5 H10.5" stroke="var(--white)" stroke-width="0.7"/><ellipse cx="6" cy="6" rx="2.5" ry="5.5" fill="none" stroke="var(--white)" stroke-width="0.7"/></svg>
          www.brightvaleholdings.com
        </li>
      </ul>
    </div>
    <div class="brand-name">
      <span class="brand-name__mark"></span>
      <div class="brand-name__text">
        <span class="brand-name__line1">Brightvale</span>
        <span class="brand-name__line2">Holdings Limited</span>
      </div>
    </div>
  </section>
</main>
</body>
</html>
```